New Business card design to reflect rebrand

I would like a business card design with a good base colour for our new logo and also a placeholder for a profile pic of the card holder. the design needs to be editable to the point that we can easily change the picture of the person and use that design for printlarkly etc. we are looking at a metalic finish business card so will need a good base colour to bring out the finish.

Target Market(s)

prospective customers

Industry/Entity Type

Business

Contact Information for Business Card

I would like one editable design that we can change the name of the card holder and profile picture. The design need to be in a format that be send to printlarkly etc.

Our address is Fenwick Lodge, Mill Lane, Ashcombe Green, KT14 3WB Tel no. 01632 960418

Requirements
Must have
• place holder for a profile pic for the card holder. in AI or preferably PSD format

```html
<!DOCTYPE html>
<html lang="en">
<head>
<meta charset="utf-8">
<title>Corvane Workplace Services – Business Card</title>
<link href="https://fonts.googleapis.com/css2?family=Michroma&family=Open+Sans:wght@400&display=swap" rel="stylesheet">
<style>
  :root {
    --backdrop: #141414;
    --card-white: #ffffff;
    --brand-orange: #ea6206;
    --brand-navy: #41526e;
    --text-dark: #2e2e2e;
    --photo-dark: #3a3a3a;
    --photo-mid: #5a5a5a;
  }
  * { margin: 0; padding: 0; box-sizing: border-box; }
  html, body {
    width: 1200px; height: 900px; overflow: hidden;
    background: var(--backdrop);
  }
  .stage { position: relative; width: 1200px; height: 900px; }
  .card {
    position: absolute; top: 170px;
    width: 347px; height: 561px;
  }
  .card-front { left: 259px; background: var(--card-white); }
  .card-back { left: 631px; background: var(--brand-orange); }

  .profile-photo {
    position: absolute; left: 104px; top: 52px;
    width: 140px; height: 192px; border-radius: 50%;
    background: radial-gradient(ellipse at 50% 35%, var(--photo-mid), var(--photo-dark) 70%);
  }
  .front-wordmark {
    position: absolute; top: 268px; left: 0; width: 100%;
    text-align: center;
    font-family: "Michroma", sans-serif; font-size: 34px;
    color: var(--brand-navy); letter-spacing: 1px;
  }
  .holder-name {
    position: absolute; top: 359px; left: 0; width: 100%;
    text-align: center;
    font-family: "Michroma", sans-serif; font-size: 17px; letter-spacing: 1px;
  }
  .holder-name .first { color: var(--brand-orange); }
  .holder-name .last { color: var(--brand-navy); }
  .contact {
    position: absolute; top: 420px; left: 0; width: 100%;
    text-align: center;
    font-family: "Open Sans", sans-serif; font-size: 15px;
    color: var(--text-dark); line-height: 20px;
  }
  .contact .address { margin-top: 6px; }

  .back-wordmark {
    position: absolute; top: 228px; left: 0; width: 100%;
    text-align: center; color: var(--card-white);
    font-family: "Michroma", sans-serif;
  }
  .back-wordmark .name { display: block; font-size: 36px; letter-spacing: 2px; }
  .back-wordmark .tagline { display: block; margin-top: 22px; font-size: 15px; letter-spacing: 3px; }
</style>
</head>
<body>
<main class="stage">
  <section class="card card-front">
    <div class="profile-photo" role="img" aria-label="Profile photo of the card holder"></div>
    <div class="front-wordmark">CORVANE</div>
    <div class="holder-name"><span class="first">DANIEL</span> <span class="last">HARTWELL</span></div>
    <div class="contact">
      <p class="phone">01632 960418</p>
      <p class="email">info@corvane.com</p>
      <p class="address">Fenwick Lodge, Mill Lane,<br>Ashcombe Green, KT14 3WB</p>
    </div>
  </section>
  <section class="card card-back">
    <div class="back-wordmark">
      <span class="name">CORVANE</span>
      <span class="tagline">WORKPLACE SERVICES</span>
    </div>
  </section>
</main>
</body>
</html>
```